High Quality Business card for Property Management Agency - Super Classy and professional design

High Quality Business card design.

We need a business card designed for our Property Management Agency.
We are located on Sydney's Northern Beaches and manage beautiful properties along the beach and harbor.
We need a design that oozes modern, classy and professional.
I would like it to be double sided with contact details and logo on the front and just the logo on the back.

I need a print ready PDF version of the file as well as an editable photoshop (PSD) version of the file.

Logo and information details attached.

Target Market(s)

Property owners/investors, Male and Female Aged 28-65

Industry/Entity Type

Real Estate

Contact Information for Business Card

Tom Carrick
Tel: 0467 239 018
Email: tom@harvestlaneestates.com.au
Website: www.harvestlaneestates.com.au
Address: Level 2, 17 Wattlecourt Rd, Dunmarra NSW 2187

Font styles to use
Sans Serif

Requirements
Must have
• - Logo front and back
• - Business card details listed above and attached
• - Colour
Nice to have
• Sleek and professional

```html
<!DOCTYPE html>
<html lang="en">
<head>
<meta charset="utf-8">
<title>Harvest Lane Estates – Business Card</title>
<link href="https://fonts.googleapis.com/css2?family=Arimo:wght@400;700&display=swap" rel="stylesheet">
<style>
  :root {
    --stage: #e9ebec;
    --teal: #1aa3b3;
    --teal-deep: #0f7f8c;
    --teal-light: #35bccb;
    --ink: #1f2326;
    --grey-text: #6e7174;
    --card-white: #ffffff;
    --card-shade: #f1f2f2;
  }
  * { margin: 0; padding: 0; box-sizing: border-box; }
  html, body { width: 1200px; height: 900px; overflow: hidden; }
  body {
    background: var(--stage);
    font-family: "Arimo", Arial, sans-serif;
    position: relative;
  }
  .card {
    position: absolute;
    width: 600px;
    height: 367px;
    border-radius: 4px;
    box-shadow: 0 8px 24px rgba(0,0,0,0.18);
    overflow: hidden;
  }
  /* Back of card */
  .card-back {
    left: 90px;
    top: 60px;
    background: radial-gradient(ellipse at 55% 35%, var(--teal-light) 0%, var(--teal) 45%, var(--teal-deep) 100%);
  }
  .card-back .brand {
    position: absolute;
    left: 0; right: 0;
    top: 140px;
    text-align: center;
  }
  .card-back .brand-name {
    color: #ffffff;
    font-weight: 700;
    font-size: 40px;
    letter-spacing: 0.5px;
    text-transform: uppercase;
  }
  .card-back .brand-web {
    margin-top: 10px;
    color: #16363b;
    font-size: 15px;
    letter-spacing: 0.5px;
  }
  /* Front of card */
  .card-front {
    left: 510px;
    top: 473px;
    background: linear-gradient(160deg, var(--card-white) 0%, var(--card-white) 55%, var(--card-shade) 100%);
  }
  .card-front .brand {
    position: absolute;
    right: 34px;
    top: 58px;
    display: flex;
    align-items: center;
    gap: 12px;
  }
  .card-front .brand-mark {
    width: 18px; height: 18px;
    border-radius: 50%;
    background: var(--teal);
  }
  .card-front .brand-name {
    color: var(--ink);
    font-weight: 700;
    font-size: 30px;
    text-transform: uppercase;
    letter-spacing: 0.3px;
  }
  .holder-name {
    position: absolute;
    right: 34px;
    top: 184px;
    color: var(--teal);
    font-weight: 700;
    font-size: 22px;
    text-transform: uppercase;
    letter-spacing: 0.5px;
  }
  .rule {
    position: absolute;
    left: 0; right: 0;
    height: 2px;
    background: var(--teal);
  }
  .rule-upper { top: 218px; left: 260px; }
  .rule-lower { top: 356px; }
  .contact {
    position: absolute;
    left: 30px;
    top: 232px;
    color: var(--grey-text);
    font-size: 14px;
    line-height: 19px;
  }
  .contact .address { margin-bottom: 8px; }
  .contact-line {
    display: flex;
    align-items: center;
    gap: 8px;
    height: 20px;
  }
  .contact-line.phone { color: var(--ink); font-weight: 700; font-size: 15px; }
  .contact-line svg { width: 14px; height: 14px; flex: none; }
</style>
</head>
<body>

  <section class="card card-back" aria-label="Card back">
    <div class="brand">
      <div class="brand-name">Harvest Lane Estates</div>
      <div class="brand-web">www.harvestlaneestates.com.au</div>
    </div>
  </section>

  <section class="card card-front" aria-label="Card front">
    <div class="brand">
      <span class="brand-mark"></span>
      <span class="brand-name">Harvest Lane Estates</span>
    </div>

    <div class="holder-name">Tom Carrick</div>
    <div class="rule rule-upper"></div>

    <div class="contact">
      <div class="address">Level 2, 17 Wattlecourt Rd<br>Dunmarra NSW 2187</div>
      <div class="contact-line phone">
        <svg viewBox="0 0 14 14" aria-hidden="true">
          <circle cx="7" cy="7" r="7" fill="#1aa3b3"/>
          <path d="M4.3 3.6c.4-.3.9-.2 1.1.2l.6 1.1c.2.3.1.7-.2.9l-.4.3c.4.9 1.1 1.6 2 2l.3-.4c.2-.3.6-.4.9-.2l1.1.6c.4.2.5.7.2 1.1l-.4.5c-.4.4-1 .5-1.5.3-1.9-.8-3.3-2.2-4.1-4.1-.2-.5-.1-1.1.3-1.5z" fill="#fff"/>
        </svg>
        0467 239 018
      </div>
      <div class="contact-line">
        <svg viewBox="0 0 14 14" aria-hidden="true">
          <circle cx="7" cy="7" r="7" fill="#1aa3b3"/>
          <rect x="3.5" y="4.5" width="7" height="5" fill="#fff"/>
          <path d="M3.5 4.7 7 7.4l3.5-2.7" fill="none" stroke="#1aa3b3" stroke-width="0.8"/>
        </svg>
        tom@harvestlaneestates.com.au
      </div>
      <div class="contact-line">
        <svg viewBox="0 0 14 14" aria-hidden="true">
          <circle cx="7" cy="7" r="7" fill="#1aa3b3"/>
          <circle cx="7" cy="7" r="3.6" fill="none" stroke="#fff" stroke-width="0.9"/>
          <path d="M3.4 7h7.2M7 3.4c-1.4 1.9-1.4 5.3 0 7.2M7 3.4c1.4 1.9 1.4 5.3 0 7.2" fill="none" stroke="#fff" stroke-width="0.7"/>
        </svg>
        www.harvestlaneestates.com.au
      </div>
    </div>

    <div class="rule rule-lower"></div>
  </section>

</body>
</html>
```